https://copperwillowbrambleyard.org/

We would like the website to represent 19th century African American civil war soldier's letters. We would like the site colors to be nice and clean . Along with the layout, including a great landing page , blogs and introduction.

```html
<!DOCTYPE html>
<html lang="en">
<head>
<meta charset="utf-8">
<title>Blogs — Copper Willow Brambleyard</title>
<link rel="stylesheet" href="https://fonts.googleapis.com/css2?family=Comfortaa:wght@500;600&family=Libre+Baskerville&family=Montserrat:wght@400;500;600&family=Mulish:wght@400;700&display=swap">
<style>
:root{
  --yellow:#e9df5c;
  --navy:#0b2566;
  --night:#1c1a3e;
  --grey:#8a8a8a;
  --slate:#5a5d66;
  --white:#ffffff;
}
*{box-sizing:border-box;margin:0;padding:0}
html,body{width:1200px;height:2425px;overflow:hidden;background:var(--white)}
body{position:relative;font-family:'Montserrat',sans-serif}
.abs{position:absolute}

/* Hero */
.hero-bg{left:0;top:0;width:1200px;height:415px}
.brand{left:72px;top:32px;display:flex;align-items:center;gap:10px;color:var(--white);font-weight:600;font-size:22px}
.brand-dot{width:34px;height:34px;border-radius:50%;background:var(--white)}
.main-nav{right:40px;top:46px;display:flex;gap:26px}
.main-nav a{color:var(--yellow);text-decoration:none;font-size:14px}
.hero-title{left:0;width:1200px;top:150px;text-align:center;color:var(--yellow);font-weight:500;font-size:43px}
.hero-text{left:349px;width:510px;top:222px;color:var(--white);font-size:13.5px;line-height:24px}

/* Cards */
.card{top:585px;width:334px;height:366px;border:3px dotted var(--navy);border-radius:24px;text-align:center;overflow:hidden}
.card-icon{top:535px;width:70px;height:70px;border-radius:50%;background:var(--yellow);display:flex;align-items:center;justify-content:center}
.card-photo{position:absolute;left:44px;top:36px;width:240px;height:160px}
.card-title{position:absolute;left:0;width:328px;top:208px;font-family:'Libre Baskerville',serif;font-size:18px;line-height:26px;color:var(--slate)}
.card-cat{position:absolute;left:0;width:328px;top:282px;font-size:13px;color:var(--grey)}
.card-foot{position:absolute;left:0;bottom:0;width:328px;height:52px;background:var(--navy)}
.card-btn{position:absolute;left:8px;top:8px;width:312px;height:36px;border:1px solid #8fa0c8;color:var(--white);font-size:13px;font-weight:500;line-height:34px}

/* Posts */
.post-date{left:92px;width:107px;height:117px;background:var(--yellow);color:var(--white);font-size:15px;line-height:15px;text-align:center;padding-top:50px}
.post-date::after{content:"";position:absolute;left:0;bottom:0;width:107px;height:17px;background:var(--slate)}
.post-title{left:224px;font-family:'Comfortaa',sans-serif;font-weight:600;font-size:33px;color:var(--navy);white-space:nowrap}
.post-lead{left:224px;width:876px;font-family:'Mulish',sans-serif;font-weight:700;font-size:11px;line-height:17px;color:var(--grey)}
.post-body{left:224px;width:876px;font-family:'Mulish',sans-serif;font-size:11.4px;line-height:17px;color:#9a9a9a}
.post-more{left:957px;width:146px;height:38px;border:2px solid var(--navy);color:var(--navy);font-size:13px;display:flex;align-items:center;justify-content:center;gap:8px}

/* Footer */
.footer-bg{left:0;top:1915px;width:1200px;height:510px}
.footer-brand{left:0;width:1200px;top:2058px;display:flex;justify-content:center;align-items:center;gap:10px;color:var(--white);font-weight:600;font-size:22px}
.footer-contact{left:0;width:1200px;top:2163px;display:flex;justify-content:center;gap:16px;color:var(--white);font-size:11px}
.footer-contact span{display:flex;align-items:center;gap:8px}
.social{left:0;width:1200px;top:2234px;display:flex;justify-content:center;gap:16px}
.social span{width:28px;height:28px;border-radius:50%;background:var(--yellow)}
.footer-nav{left:0;width:1200px;top:2282px;display:flex;justify-content:center;gap:32px;color:var(--white);font-size:14px}
.footer-nav span{display:flex;align-items:center;gap:6px}
.copyright{left:0;width:1200px;top:2326px;text-align:center;color:var(--white);font-size:13px}
</style>
</head>
<body>

<svg class="abs hero-bg" viewBox="0 0 1200 415" role="img" aria-label="Sepia engraving of Civil War soldiers on horseback among trees">
  <defs>
    <linearGradient id="heroShade" x1="0" y1="0" x2="1" y2="1">
      <stop offset="0" stop-color="#6e6e6e"/>
      <stop offset="0.5" stop-color="#4a4a4a"/>
      <stop offset="1" stop-color="#5e5e5e"/>
    </linearGradient>
  </defs>
  <polygon points="0,0 1200,0 1200,333 600,415 0,333" fill="url(#heroShade)"/>
</svg>

<div class="abs brand"><span class="brand-dot"></span>Copper Willow Brambleyard</div>
<nav class="abs main-nav"><a href="#">Home</a><a href="#">About</a><a href="#">Blog</a><a href="#">Contact</a></nav>
<h1 class="abs hero-title">Blogs</h1>
<p class="abs hero-text">Lorem ipsum dolor sit amet, consectetur adipiscing elit. Ut elit tellus, luctus nec ullamcorper mattis, pulvinar dapibus leo.</p>

<div class="abs card" style="left:80px">
  <div class="card-photo" role="img" aria-label="Handwritten letter on aged paper" style="background:radial-gradient(ellipse at 40% 40%,#d8b98c,#a57d52 70%,#7d5a37)"></div>
  <div class="card-title">"I Heard From My Brother John...He Is Not Dead"</div>
  <div class="card-cat">In "Pvt. Elias Thorne, 14th Ohio USCT"</div>
  <div class="card-foot"><div class="card-btn">Read More</div></div>
</div>
<div class="abs card" style="left:433px">
  <div class="card-photo" role="img" aria-label="Fountain pen writing on lined paper" style="background:radial-gradient(ellipse at 55% 55%,#e2e1db,#b4b3ad 60%,#6f6f6b)"></div>
  <div class="card-title" style="top:220px">"I Was Glad To Hear From Home"</div>
  <div class="card-cat">In "Pvt. Elias Thorne, 14th Ohio USCT"</div>
  <div class="card-foot"><div class="card-btn">Read More</div></div>
</div>
<div class="abs card" style="left:786px">
  <div class="card-photo" role="img" aria-label="Old printed documents on a desk" style="background:linear-gradient(180deg,#2a2623,#6f6252 45%,#a8967c 65%,#3a332c)"></div>
  <div class="card-title">"I'm Well And Doing Well As A Soldier Can Expect..."</div>
  <div class="card-cat">In "Pvt. Elias Thorne, 14th Ohio USCT"</div>
  <div class="card-foot"><div class="card-btn">Read More</div></div>
</div>

<div class="abs card-icon" style="left:212px"><svg width="32" height="32" viewBox="0 0 32 32"><rect x="3" y="6" width="26" height="23" rx="3" fill="#fff"/><rect x="9" y="2" width="3" height="7" fill="#fff"/><rect x="20" y="2" width="3" height="7" fill="#fff"/><g fill="var(--yellow)"><rect x="7" y="14" width="4" height="4"/><rect x="14" y="14" width="4" height="4"/><rect x="21" y="14" width="4" height="4"/><rect x="7" y="21" width="4" height="4"/><rect x="14" y="21" width="4" height="4"/><rect x="21" y="21" width="4" height="4"/></g></svg></div>
<div class="abs card-icon" style="left:565px"><svg width="32" height="32" viewBox="0 0 32 32"><rect x="3" y="6" width="26" height="23" rx="3" fill="#fff"/><rect x="9" y="2" width="3" height="7" fill="#fff"/><rect x="20" y="2" width="3" height="7" fill="#fff"/><g fill="var(--yellow)"><rect x="7" y="14" width="4" height="4"/><rect x="14" y="14" width="4" height="4"/><rect x="21" y="14" width="4" height="4"/><rect x="7" y="21" width="4" height="4"/><rect x="14" y="21" width="4" height="4"/><rect x="21" y="21" width="4" height="4"/></g></svg></div>
<div class="abs card-icon" style="left:918px"><svg width="32" height="32" viewBox="0 0 32 32"><rect x="3" y="6" width="26" height="23" rx="3" fill="#fff"/><rect x="9" y="2" width="3" height="7" fill="#fff"/><rect x="20" y="2" width="3" height="7" fill="#fff"/><g fill="var(--yellow)"><rect x="7" y="14" width="4" height="4"/><rect x="14" y="14" width="4" height="4"/><rect x="21" y="14" width="4" height="4"/><rect x="7" y="21" width="4" height="4"/><rect x="14" y="21" width="4" height="4"/><rect x="21" y="21" width="4" height="4"/></g></svg></div>

<div class="abs post-date" style="top:1076px">Dec<br>19th</div>
<h2 class="abs post-title" style="top:1058px">"I Heard From My Brother John...He Is Not Dead"</h2>
<p class="abs post-lead" style="top:1107px">Lorem ipsum dolor sit amet, consectetur adipiscing elit. Phasellus sit amet odio porttitor, rutrum ligula ac, placerat dui. Morbi porttitor ac eros nec suscipit. Mauris hendrerit egestas tincidunt.</p>
<p class="abs post-body" style="top:1158px">Quisque dictum dolor sem, eu viverra ligula vulputate in. Nullam faucibus venenatis odio. Vestibulum ex dui, pulvinar ut finibus et, sollicitudin non lorem. Quisque dictum dolor sem, eu viverra ligula vulputate in. Nullam faucibus venenatis odio. Vestibulum ex dui, pulvinar ut finibus et, sollicitudin non lorem. Quisque dictum dolor sem, eu viverra ligula vulputate in. Nullam faucibus venenatis odio. Vestibulum ex dui, pulvinar ut finibus et, sollicitudin non lorem. Quisque dictum dolor sem, eu viverra ligula vulputate in. Nullam faucibus venenatis odio. Vestibulum ex dui, pulvinar ut finibus et, sollicitudin non lorem. Quisque dictum dolor sem, eu viverra ligula vulputate in. Nullam faucibus venenatis odio.</p>
<div class="abs post-more" style="top:1269px">Read More <svg width="12" height="12" viewBox="0 0 12 12"><circle cx="6" cy="6" r="6" fill="var(--navy)"/><path d="M3 6h5M6 3.5 8.5 6 6 8.5" stroke="#fff" stroke-width="1.6" fill="none"/></svg></div>

<div class="abs post-date" style="top:1339px">Jan<br>14th</div>
<h2 class="abs post-title" style="top:1321px">"I Was Glad To Hear From Home"</h2>
<p class="abs post-lead" style="top:1370px">Lorem ipsum dolor sit amet, consectetur adipiscing elit. Phasellus sit amet odio porttitor, rutrum ligula ac, placerat dui. Morbi porttitor ac eros nec suscipit. Mauris hendrerit egestas tincidunt.</p>
<p class="abs post-body" style="top:1421px">Quisque dictum dolor sem, eu viverra ligula vulputate in. Nullam faucibus venenatis odio. Vestibulum ex dui, pulvinar ut finibus et, sollicitudin non lorem. Quisque dictum dolor sem, eu viverra ligula vulputate in. Nullam faucibus venenatis odio. Vestibulum ex dui, pulvinar ut finibus et, sollicitudin non lorem. Quisque dictum dolor sem, eu viverra ligula vulputate in. Nullam faucibus venenatis odio. Vestibulum ex dui, pulvinar ut finibus et, sollicitudin non lorem. Quisque dictum dolor sem, eu viverra ligula vulputate in. Nullam faucibus venenatis odio. Vestibulum ex dui, pulvinar ut finibus et, sollicitudin non lorem. Quisque dictum dolor sem, eu viverra ligula vulputate in. Nullam faucibus venenatis odio.</p>
<div class="abs post-more" style="top:1532px">Read More <svg width="12" height="12" viewBox="0 0 12 12"><circle cx="6" cy="6" r="6" fill="var(--navy)"/><path d="M3 6h5M6 3.5 8.5 6 6 8.5" stroke="#fff" stroke-width="1.6" fill="none"/></svg></div>

<div class="abs post-date" style="top:1602px">Feb<br>18th</div>
<h2 class="abs post-title" style="top:1584px">"I'm Well And Doing Well As A Soldier Can Expect..."</h2>
<p class="abs post-lead" style="top:1633px">Lorem ipsum dolor sit amet, consectetur adipiscing elit. Phasellus sit amet odio porttitor, rutrum ligula ac, placerat dui. Morbi porttitor ac eros nec suscipit. Mauris hendrerit egestas tincidunt.</p>
<p class="abs post-body" style="top:1684px">Quisque dictum dolor sem, eu viverra ligula vulputate in. Nullam faucibus venenatis odio. Vestibulum ex dui, pulvinar ut finibus et, sollicitudin non lorem. Quisque dictum dolor sem, eu viverra ligula vulputate in. Nullam faucibus venenatis odio. Vestibulum ex dui, pulvinar ut finibus et, sollicitudin non lorem. Quisque dictum dolor sem, eu viverra ligula vulputate in. Nullam faucibus venenatis odio. Vestibulum ex dui, pulvinar ut finibus et, sollicitudin non lorem. Quisque dictum dolor sem, eu viverra ligula vulputate in. Nullam faucibus venenatis odio. Vestibulum ex dui, pulvinar ut finibus et, sollicitudin non lorem. Quisque dictum dolor sem, eu viverra ligula vulputate in. Nullam faucibus venenatis odio.</p>
<div class="abs post-more" style="top:1795px">Read More <svg width="12" height="12" viewBox="0 0 12 12"><circle cx="6" cy="6" r="6" fill="var(--navy)"/><path d="M3 6h5M6 3.5 8.5 6 6 8.5" stroke="#fff" stroke-width="1.6" fill="none"/></svg></div>

<svg class="abs footer-bg" viewBox="0 0 1200 510" role="img" aria-label="Silhouettes of marching soldiers on a dark navy background">
  <defs>
    <linearGradient id="footShade" x1="0" y1="0" x2="0" y2="1">
      <stop offset="0" stop-color="#1d1b40"/>
      <stop offset="0.55" stop-color="#1d1b40"/>
      <stop offset="1" stop-color="#25234a"/>
    </linearGradient>
  </defs>
  <polygon points="0,113 600,0 1200,113 1200,510 0,510" fill="url(#footShade)"/>
</svg>

<div class="abs footer-brand"><span class="brand-dot"></span>Copper Willow Brambleyard</div>
<div class="abs footer-contact">
  <span><svg width="12" height="12" viewBox="0 0 12 12"><path d="M2 1l2.5 0 1 3-1.5 1a7 7 0 0 0 3 3l1-1.5 3 1V11c-5 0-9-4-9-9z" fill="var(--yellow)"/></svg>+0147258369</span>
  <span><svg width="14" height="11" viewBox="0 0 14 11"><rect width="14" height="11" rx="1" fill="var(--yellow)"/><path d="M1 1l6 5 6-5" stroke="var(--night)" stroke-width="1.3" fill="none"/></svg>hello@copperwillowbrambleyard.org</span>
</div>
<div class="abs social"><span></span><span></span><span></span><span></span><span></span></div>
<nav class="abs footer-nav">
  <span><svg width="14" height="12" viewBox="0 0 14 12"><path d="M7 0 14 6h-2v6H9V8H5v4H2V6H0z" fill="var(--yellow)"/></svg>Home</span>
  <span><svg width="10" height="13" viewBox="0 0 10 13"><path d="M0 0h10v13L5 9 0 13z" fill="var(--yellow)"/></svg>About</span>
  <span><svg width="12" height="12" viewBox="0 0 12 12"><rect width="12" height="12" rx="2" fill="var(--yellow)"/><rect x="3" y="3" width="6" height="1.5" fill="var(--night)"/><rect x="3" y="6" width="6" height="1.5" fill="var(--night)"/></svg>Blog</span>
  <span><svg width="15" height="11" viewBox="0 0 15 11"><rect width="15" height="11" rx="1" fill="var(--yellow)"/><circle cx="4.5" cy="4.5" r="2" fill="var(--night)"/><rect x="8" y="3" width="5" height="1.3" fill="var(--night)"/><rect x="8" y="6" width="5" height="1.3" fill="var(--night)"/></svg>Contact</span>
</nav>
<p class="abs copyright">Copyright © 2020 My Blog</p>

</body>
</html>
```